Business Broker Website

Hi.
I need a new design done for a business broker website. An example of the style of website I like is https://marlowvantage.example/
The menu needs to be :
* Home
* Businesses for Sale
* What we do
* Our people
* Industries
* Blog
* Confidentiality
* Contact
The home page needs to include a section saying 'businesses sold' with each having a photo, heading and short description. It also needs to have a place to show a video which I have attached so you can take a screenshot to put it on the page.
The content on the home page needs to be as follows:
Harbourline Ventures Group are a boutique brokerage business, specializing in the sales and marketing of SME businesses throughout Queensland and, the Northern Territory
who we are
Welcome to Harbourline Ventures Group. Our specialization is in the marketing and acquisition of closely held businesses throughout Queensland and the Northern Territory. We concentrate in SME businesses in the turnovers of approximately $1,000,000 to $10,000,000 +.
The combined business experience and industry knowledge of our principal is unparalleled and fully committed to a “customer first always” approach to doing business.
Our seller’s benefit from a multi-faceted strategic marketing plan, custom prepared for each seller, no two marketing campaigns are the same. This assures maximum exposure to well-qualified Buyers, while strictly maintaining confidentiality.
We have the comprehensive knowledge and resources to help our Buyers identify their perfect business acquisition– perhaps even if that business is not currently listed for sale!
"the whole secret of a successful life is to find out what is one's destiny to do, and then do it." walter pryce
people looking to buy or sell businesses
1 page

```html
<!DOCTYPE html>
<html lang="en">
<head>
<meta charset="utf-8">
<title>Harbourline Ventures Group</title>
<link href="https://fonts.googleapis.com/css2?family=Open+Sans:wght@400;600;700;800&display=swap" rel="stylesheet">
<style>
:root{
  --purple:#5a3d8c;
  --purple-dark:#45306e;
  --ink:#2b2b2b;
  --muted:#6f6f6f;
  --line:#e3e3e3;
  --dark:#1f1f22;
  --dark-2:#2c2c30;
  --footer:#3a3a3e;
  --footer-2:#2f2f33;
  --white:#ffffff;
}
*{box-sizing:border-box;margin:0;padding:0}
html,body{width:1200px;height:2540px;overflow:hidden}
body{font-family:"Open Sans",Arial,sans-serif;color:var(--ink);background:var(--white);font-size:12px;line-height:1.6}
.wrap{width:960px;margin:0 auto}
a{color:inherit;text-decoration:none}

/* header */
.topbar{height:26px;display:flex;justify-content:center;gap:0;font-size:10px}
.topbar span{background:var(--purple);color:var(--white);padding:5px 18px;font-weight:600}
.topbar span + span{background:var(--purple-dark)}
.header{height:62px;display:flex;align-items:center;justify-content:space-between}
.brand{display:flex;align-items:center;gap:8px;color:var(--purple);font-weight:800;font-size:19px;letter-spacing:.2px}
.brand-dot{width:26px;height:26px;border-radius:50%;background:var(--purple)}
.nav{display:flex;align-items:center;gap:24px;font-size:10.5px;font-weight:700;text-transform:uppercase;color:#444}
.nav .active{color:var(--purple)}
.nav-search{width:24px;height:24px;border-radius:50%;background:var(--purple);display:flex;align-items:center;justify-content:center}

/* hero */
.hero{position:relative;height:400px;background:linear-gradient(115deg,#dfe3ea 0%,#b9c0cc 40%,#7c8696 70%,#c8ced8 100%);color:var(--white);text-align:center}
.hero-inner{position:absolute;left:0;right:0;top:110px}
.hero h1{font-size:34px;font-weight:800;text-shadow:0 1px 3px rgba(0,0,0,.25)}
.hero p{width:560px;margin:14px auto 0;font-size:13px;line-height:1.5}
.hero-mouse{position:absolute;left:50%;bottom:30px;margin-left:-9px}

/* section titles */
.sec-title{text-align:center;font-size:24px;font-weight:700;color:var(--ink)}
.sec-sub{width:640px;margin:10px auto 0;text-align:center;color:var(--muted);font-size:10.5px;line-height:1.5}

/* business for sale */
.sales{padding:40px 0 34px}
.cards{display:flex;gap:20px;margin-top:26px}
.card{flex:1}
.card-head{display:flex;align-items:center;gap:8px;font-weight:700;font-size:13px;margin-bottom:8px}
.card-icon{width:28px;height:28px;border-radius:50%;background:var(--purple);display:flex;align-items:center;justify-content:center}
.card-photo{height:112px}
.card p{margin-top:10px;font-size:10.5px;color:var(--muted);line-height:1.5}
.more{display:inline-block;margin-top:10px;font-size:9.5px;font-weight:700;color:var(--ink);text-transform:uppercase}
.more::after{content:" \2192";color:var(--purple)}

/* what we do */
.whatwedo{display:flex;gap:30px}
.office{width:480px;height:270px;background:linear-gradient(135deg,#dfe7ef,#b9c7d6 55%,#e6dccb);position:relative}
.play{position:absolute;left:50%;top:50%;width:46px;height:46px;margin:-23px 0 0 -23px;border-radius:50%;background:rgba(255,255,255,.9);display:flex;align-items:center;justify-content:center}
.wwd-text{flex:1;padding-top:6px}
.wwd-text h2{font-size:24px;font-weight:700}
.wwd-text p{margin-top:12px;font-size:10.5px;color:var(--muted);line-height:1.55}
.btn{display:inline-block;margin-top:16px;background:var(--purple);color:var(--white);font-weight:700;font-size:11px;padding:9px 22px;border-radius:20px}
.features{display:flex;background:var(--dark);color:var(--white);height:110px}
.feature{flex:1;padding:22px 20px;border-right:1px solid #37373c}
.feature:last-child{border-right:0}
.feature h3{display:flex;align-items:center;gap:8px;font-size:12px;font-weight:700}
.feature p{margin-top:8px;font-size:9.5px;color:#b6b6bb;line-height:1.5}

/* people */
.people{padding:50px 0 0}
.people-row{display:flex;margin-top:26px}
.people-row div{flex:1;height:140px}

/* sell or buy */
.sellbuy{margin-top:36px;height:240px;background:linear-gradient(100deg,#121214 0%,#1d1d20 45%,#3a302c 70%,#17171a 100%);color:var(--white)}
.sellbuy .wrap{display:flex;justify-content:space-between;align-items:center;height:100%}
.sb-text{width:340px}
.sb-text h2{font-size:15px;font-weight:700}
.sb-text p{margin-top:10px;font-size:10px;color:#c9c9cc;line-height:1.55}
.form{width:300px;background:rgba(255,255,255,.08);padding:16px;display:grid;grid-template-columns:1fr 1fr;gap:8px}
.field{height:26px;background:var(--white);font-size:9.5px;color:#999;padding:6px 8px}
.field.full{grid-column:1 / 3}
.field.tall{height:50px}
.form .submit{grid-column:1 / 3;background:var(--purple);color:var(--white);text-align:center;font-weight:700;font-size:10px;padding:7px}

/* blog */
.blog{padding:44px 0 40px}
.posts{display:flex;gap:30px;margin-top:28px}
.post{flex:1}
.post-photo{height:150px;position:relative}
.tags{position:absolute;left:10px;bottom:10px;display:flex;gap:4px}
.tags span{background:var(--purple);color:var(--white);font-size:8.5px;font-weight:700;padding:2px 8px}
.post h3{margin-top:12px;font-size:12.5px;font-weight:700;line-height:1.35}
.post .meta{margin-top:6px;font-size:9.5px;color:var(--muted)}

/* footer */
.newsletter{background:var(--footer);color:var(--white);height:90px}
.newsletter .wrap{display:flex;justify-content:space-between;align-items:center;height:100%}
.newsletter h2{font-size:15px;font-weight:700;text-transform:uppercase}
.newsletter p{font-size:9.5px;color:#c4c4c8}
.subscribe{display:flex;align-items:center;gap:10px}
.subscribe .input{width:240px;height:30px;background:var(--white);color:#999;font-size:10px;padding:8px 12px}
.subscribe .btn{margin:0;border-radius:16px;font-size:10px;padding:8px 20px}
.footer{background:var(--footer-2);color:#c4c4c8;height:292px;padding-top:34px}
.cols{display:flex;gap:40px}
.col{flex:1;font-size:10px;line-height:1.6}
.col:first-child{flex:1.5}
.col h4{color:var(--white);font-size:11px;font-weight:700;text-transform:uppercase;margin-bottom:12px}
.col li{list-style:none;margin-bottom:6px}
.col li::before{content:"\203A  ";color:var(--purple)}
.contact-list li::before{content:""}
.bottom{margin-top:34px;padding-top:16px;border-top:1px solid #46464b;display:flex;justify-content:space-between;align-items:center;font-size:9.5px}
.social{display:flex;gap:8px}
.social span{width:18px;height:18px;border-radius:50%;background:#55555b}
</style>
</head>
<body>

<div class="topbar"><span>Contact: +61 7 5550 0148</span><span>hello@harbourline.example</span></div>
<header class="wrap header">
  <div class="brand"><span class="brand-dot"></span>Harbourline Ventures Group</div>
  <nav class="nav">
    <a class="active">Home</a><a>Businesses</a><a>What we do</a><a>Industries</a><a>Blog</a><a>Contact</a><a>Our people</a>
    <span class="nav-search"><svg width="12" height="12" viewBox="0 0 12 12"><circle cx="5" cy="5" r="3.5" fill="none" stroke="#fff" stroke-width="1.5"/><line x1="7.6" y1="7.6" x2="11" y2="11" stroke="#fff" stroke-width="1.5"/></svg></span>
  </nav>
</header>

<section class="hero" role="img" aria-label="Photo of glass office towers seen from below">
  <div class="hero-inner">
    <h1>The Harbourline Ventures Group</h1>
    <p>A boutique brokerage business, specializing in the sales and marketing of SME businesses throughout Queensland and the Northern Territory.</p>
  </div>
  <svg class="hero-mouse" width="18" height="28" viewBox="0 0 18 28"><rect x="1" y="1" width="16" height="26" rx="8" fill="none" stroke="#fff" stroke-width="1.5"/><line x1="9" y1="6" x2="9" y2="11" stroke="#fff" stroke-width="1.5"/></svg>
</section>

<section class="wrap sales">
  <h2 class="sec-title">Business for sales</h2>
  <p class="sec-sub">Well-established SME businesses across Queensland and the Northern Territory, marketed with strict confidentiality to qualified buyers. Browse current listings by industry below and contact us for details.</p>
  <div class="cards">
    <article class="card">
      <div class="card-head"><span class="card-icon"><svg width="16" height="12" viewBox="0 0 16 12"><rect x="0" y="1" width="10" height="7" fill="#fff"/><path d="M10 3h3l3 3v2h-6z" fill="#fff"/><circle cx="3.5" cy="10" r="1.6" fill="#fff"/><circle cx="12.5" cy="10" r="1.6" fill="#fff"/></svg></span>Transport</div>
      <div class="card-photo" role="img" aria-label="Photo of a transport depot" style="background:linear-gradient(135deg,#6f7a86,#2f3a46)"></div>
      <p>Regional freight and logistics operator with long-term contracts and a modern fleet.</p>
      <a class="more">Read more</a>
    </article>
    <article class="card">
      <div class="card-head"><span class="card-icon"><svg width="14" height="14" viewBox="0 0 14 14"><circle cx="7" cy="4" r="3" fill="#fff"/><path d="M2 14c0-4 2-6 5-6s5 2 5 6z" fill="#fff"/></svg></span>Child care</div>
      <div class="card-photo" role="img" aria-label="Photo of colourful children's play materials" style="background:linear-gradient(135deg,#d9608a,#4c8fd6 55%,#e8c449)"></div>
      <p>Licensed early learning centre with strong occupancy and experienced staff.</p>
      <a class="more">Read more</a>
    </article>
    <article class="card">
      <div class="card-head"><span class="card-icon"><svg width="14" height="14" viewBox="0 0 14 14"><circle cx="7" cy="7" r="4.5" fill="none" stroke="#fff" stroke-width="2.5" stroke-dasharray="2.4 1.2"/><circle cx="7" cy="7" r="1.6" fill="#fff"/></svg></span>Engineering</div>
      <div class="card-photo" role="img" aria-label="Photo of an engineer at work in a workshop" style="background:linear-gradient(135deg,#8a7a5c,#3b3a36)"></div>
      <p>Precision fabrication business servicing mining and construction clients.</p>
      <a class="more">Read more</a>
    </article>
    <article class="card">
      <div class="card-head"><span class="card-icon"><svg width="12" height="12" viewBox="0 0 12 12"><path d="M4 0h4v4h4v4H8v4H4V8H0V4h4z" fill="#fff"/></svg></span>Medical</div>
      <div class="card-photo" role="img" aria-label="Photo of a medical practitioner in a clinic" style="background:linear-gradient(135deg,#dfe4ea,#8fa2b4)"></div>
      <p>Established allied health clinic with loyal patient base and growth potential.</p>
      <a class="more">Read more</a>
    </article>
  </div>
</section>

<section class="wrap">
  <div class="whatwedo">
    <div class="office" role="img" aria-label="Illustration of people working in a modern office, video preview">
      <span class="play"><svg width="14" height="16" viewBox="0 0 14 16"><path d="M2 1l11 7-11 7z" fill="#5a3d8c"/></svg></span>
    </div>
    <div class="wwd-text">
      <h2>What we do</h2>
      <p>Welcome to Harbourline Ventures Group. Our specialization is in the marketing and acquisition of closely held businesses throughout Queensland and the Northern Territory. We concentrate in SME businesses in the turnovers of approximately $1,000,000 to $10,000,000 +.</p>
      <p>Our seller's benefit from a multi-faceted strategic marketing plan, custom prepared for each seller, no two marketing campaigns are the same. This assures maximum exposure to well-qualified Buyers, while strictly maintaining confidentiality.</p>
      <a class="btn">View More</a>
    </div>
  </div>
  <div class="features">
    <div class="feature"><h3><svg width="14" height="14" viewBox="0 0 14 14"><circle cx="7" cy="7" r="6" fill="#5a3d8c"/><path d="M4 7l2 2 4-4" stroke="#fff" stroke-width="1.6" fill="none"/></svg>Specialists</h3><p>Focused on closely held SME businesses in Queensland and the Territory.</p></div>
    <div class="feature"><h3><svg width="14" height="14" viewBox="0 0 14 14"><rect x="1" y="3" width="12" height="9" fill="#5a3d8c"/><rect x="5" y="1" width="4" height="2" fill="#5a3d8c"/></svg>Strategic marketing</h3><p>A custom marketing plan prepared for every seller we represent.</p></div>
    <div class="feature"><h3><svg width="14" height="14" viewBox="0 0 14 14"><rect x="3" y="6" width="8" height="7" fill="#5a3d8c"/><path d="M4.5 6V4a2.5 2.5 0 015 0v2" stroke="#5a3d8c" stroke-width="1.6" fill="none"/></svg>Confidentiality</h3><p>Maximum buyer exposure while strictly protecting your privacy.</p></div>
    <div class="feature"><h3><svg width="14" height="14" viewBox="0 0 14 14"><path d="M5 0h4v5h5v4H9v5H5V9H0V5h5z" fill="#5a3d8c"/></svg>Buyers</h3><p>Helping buyers find the right acquisition, listed or not.</p></div>
  </div>
</section>

<section class="people">
  <h2 class="sec-title">Our People</h2>
  <div class="wrap people-row">
    <div role="img" aria-label="Photo of a broker in a meeting" style="background:linear-gradient(135deg,#c9b8a2,#7b6a58)"></div>
    <div role="img" aria-label="Photo of team members shaking hands" style="background:linear-gradient(135deg,#dad7d2,#8d8a86)"></div>
    <div role="img" aria-label="Photo of a consultant at a desk" style="background:linear-gradient(135deg,#a99886,#5d5044)"></div>
    <div role="img" aria-label="Photo of a business discussion" style="background:linear-gradient(135deg,#d5d3cf,#6e7076)"></div>
    <div role="img" aria-label="Photo of colleagues reviewing documents" style="background:linear-gradient(135deg,#c3b5a4,#6b5e52)"></div>
  </div>
</section>

<section class="sellbuy" role="img" aria-label="Photo of a winding road at night with light trails">
  <div class="wrap">
    <div class="sb-text">
      <h2>Sell or Buy Your Business</h2>
      <p>We have the comprehensive knowledge and resources to help our Buyers identify their perfect business acquisition, perhaps even if that business is not currently listed for sale. Sellers receive a tailored plan and qualified buyer exposure.</p>
      <p>"The whole secret of a successful life is to find out what is one's destiny to do, and then do it." Walter Pryce</p>
    </div>
    <div class="form">
      <div class="field">First Name</div><div class="field">Last Name</div>
      <div class="field">Email</div><div class="field">Phone</div>
      <div class="field full tall">Message</div>
      <div class="submit">Submit</div>
    </div>
  </div>
</section>

<section class="wrap blog">
  <h2 class="sec-title">Blog Post</h2>
  <div class="posts">
    <article class="post">
      <div class="post-photo" role="img" aria-label="Photo of green crops in a field" style="background:linear-gradient(135deg,#7fb04a,#3e6a2a)"><div class="tags"><span>NEWS</span><span>BLOG</span></div></div>
      <h3>Journeys from Rural Businesses to New Owners</h3>
      <p class="meta">12 March &middot; 3 comments</p>
    </article>
    <article class="post">
      <div class="post-photo" role="img" aria-label="Photo of hands with coloured pencils" style="background:linear-gradient(135deg,#e3c79a,#c0704a 60%,#6a8fbf)"><div class="tags"><span>NEWS</span><span>BLOG</span></div></div>
      <h3>Journeys from Family Firms to New Investors</h3>
      <p class="meta">08 March &middot; 5 comments</p>
    </article>
    <article class="post">
      <div class="post-photo" role="img" aria-label="Photo of a roadside service station" style="background:linear-gradient(135deg,#8fb3d6,#c8413c 60%,#4a4a50)"><div class="tags"><span>NEWS</span><span>BLOG</span></div></div>
      <h3>Journeys from Retail Sites to New Operators</h3>
      <p class="meta">02 March &middot; 2 comments</p>
    </article>
  </div>
</section>

<section class="newsletter">
  <div class="wrap">
    <div><h2>Subscribe our newsletter</h2><p>Get the latest listings and market updates in your inbox.</p></div>
    <div class="subscribe"><span class="input">Your email address</span><a class="btn">Subscribe</a></div>
  </div>
</section>

<footer class="footer">
  <div class="wrap">
    <div class="cols">
      <div class="col"><h4>About us</h4><p>Harbourline Ventures Group are a boutique brokerage business, specializing in the sales and marketing of SME businesses throughout Queensland and the Northern Territory, with a customer first always approach.</p></div>
      <div class="col"><h4>Useful links</h4><ul><li>Home</li><li>What we do</li><li>Our people</li><li>Blog</li><li>Contact</li></ul></div>
      <div class="col"><h4>Services</h4><ul><li>Transport</li><li>Child care</li><li>Engineering</li><li>Medical</li><li>Retail</li></ul></div>
      <div class="col"><h4>Contact info</h4><ul class="contact-list"><li>14 Quayside Lane, Brisbane QLD</li><li>+61 7 5550 0148</li><li>hello@harbourline.example</li></ul></div>
    </div>
    <div class="bottom">
      <span>Copyright &copy; 2024 Harbourline Ventures Group. All rights reserved.</span>
      <div class="social"><span></span><span></span><span></span><span></span></div>
    </div>
  </div>
</footer>

</body>
</html>
```